I'm a magician . hypnotist also a good barber. I need this all to be shown in good detail on the cards.

Industry/Entity Type

Magician

Contact Information for Business Card

Magician/ hypnotist/barber Rowan Pitt. One of the best. Tel 07421 736204
Email.Trickshears48@fernmail.example
Title of card spell chap.

```html
<!DOCTYPE html>
<html lang="en">
<head>
<meta charset="utf-8">
<title>Spell Chap – Business Card</title>
<link rel="stylesheet" href="https://fonts.googleapis.com/css2?family=Poiret+One&family=Noticia+Text:ital@1&family=Josefin+Sans:wght@400&display=swap">
<style>
  :root {
    --frame: #56696b;
    --bg-top: #0b0d0e;
    --bg-mid: #3f4c4f;
    --bg-low: #8c9ea3;
    --bg-bottom: #d9e4e6;
    --title: #c9d6d8;
    --light-text: #f2f5f5;
    --dark-text: #2f3a3c;
    --icon-light: #f4f7f7;
  }
  * { margin: 0; padding: 0; box-sizing: border-box; }
  html, body {
    width: 1200px;
    height: 686px;
    overflow: hidden;
    background: #ffffff;
  }
  .card {
    position: relative;
    width: 1200px;
    height: 686px;
    background: #ffffff;
  }
  .card-face {
    position: absolute;
    left: 19px;
    top: 19px;
    width: 1162px;
    height: 645px;
    border: 5px solid var(--frame);
    background: linear-gradient(180deg,
      var(--bg-top) 0%,
      #1a2022 22%,
      var(--bg-mid) 45%,
      var(--bg-low) 70%,
      var(--bg-bottom) 100%);
    overflow: hidden;
  }
  .smoke-texture {
    position: absolute;
    inset: 0;
    background:
      radial-gradient(ellipse 60% 30% at 30% 75%, rgba(230,240,242,0.25), transparent 70%),
      radial-gradient(ellipse 50% 25% at 75% 85%, rgba(230,240,242,0.3), transparent 70%),
      radial-gradient(ellipse 40% 30% at 80% 20%, rgba(120,140,145,0.15), transparent 70%);
  }
  .card-title {
    position: absolute;
    left: 0;
    right: 0;
    top: 48px;
    text-align: center;
    font-family: "Poiret One", sans-serif;
    font-size: 112px;
    line-height: 1;
    color: var(--title);
    letter-spacing: 2px;
  }
  .tagline {
    position: absolute;
    left: 140px;
    right: 140px;
    top: 262px;
    text-align: center;
    font-family: "Noticia Text", serif;
    font-style: italic;
    font-size: 40px;
    line-height: 52px;
    color: var(--dark-text);
  }
  .tagline .roles { color: var(--light-text); }
  .contact {
    position: absolute;
    top: 560px;
    display: flex;
    align-items: center;
    gap: 14px;
    color: var(--dark-text);
  }
  .contact-email {
    left: 63px;
    font-family: "Noticia Text", serif;
    font-style: italic;
    font-size: 28px;
  }
  .contact-phone {
    left: 846px;
    font-family: "Josefin Sans", sans-serif;
    font-size: 30px;
  }
  .icon { display: block; }
</style>
</head>
<body>
  <div class="card">
    <div class="card-face">
      <div class="smoke-texture" role="img" aria-label="Soft smoky cloud texture fading from dark to pale grey-blue"></div>

      <h1 class="card-title">Spell Chap</h1>

      <p class="tagline"><span class="roles">Magician/ hypnotist/</span>barber Rowan Pitt. One of the best.</p>

      <div class="contact contact-email">
        <svg class="icon" width="56" height="38" viewBox="0 0 56 38" aria-hidden="true">
          <rect x="1.5" y="1.5" width="53" height="35" fill="none" stroke="var(--icon-light)" stroke-width="2"/>
          <polyline points="1.5,1.5 28,22 54.5,1.5" fill="none" stroke="var(--icon-light)" stroke-width="2"/>
          <line x1="1.5" y1="36.5" x2="21" y2="17" stroke="var(--icon-light)" stroke-width="2"/>
          <line x1="54.5" y1="36.5" x2="35" y2="17" stroke="var(--icon-light)" stroke-width="2"/>
        </svg>
        <span>Trickshears48@fernmail.example</span>
      </div>

      <div class="contact contact-phone">
        <svg class="icon" width="28" height="48" viewBox="0 0 28 48" aria-hidden="true">
          <rect x="0" y="0" width="28" height="48" rx="4" fill="var(--icon-light)"/>
          <rect x="4" y="5" width="20" height="20" fill="#6f8084"/>
          <g fill="#6f8084">
            <rect x="4" y="30" width="5" height="3"/><rect x="11.5" y="30" width="5" height="3"/><rect x="19" y="30" width="5" height="3"/>
            <rect x="4" y="36" width="5" height="3"/><rect x="11.5" y="36" width="5" height="3"/><rect x="19" y="36" width="5" height="3"/>
            <rect x="4" y="42" width="5" height="3"/><rect x="11.5" y="42" width="5" height="3"/><rect x="19" y="42" width="5" height="3"/>
          </g>
        </svg>
        <span>07421 736204</span>
      </div>
    </div>
  </div>
</body>
</html>
```